Equipment Supplier Brochure Needed

We need a professional one-page, front-and-back brochure for Tovrix, an equipment and parts supplier serving peanut shelling and processing facilities across the Southeast. This brochure will be used as a leave-behind with plant managers and procurement teams, so it must look clean, modern, and visually strong.

Front of brochure:

Tovrix logo and strong branding

Brief headline/summary of what Tovrix does

Product category overview listed on the front (high-level, clean layout)

Flat Screens (slot, round, herringbone, square, Style 1 & Style 2)

Sheller Grates

Ripple Screens

Sheller Bars

Eccentric Bearing Housings

Eccentric Shafts

Rebuilt Machines

Ducts

Sprockets

Rubber Gum Balls

Fiberglass

Mellin Pike Reels

Elevator Buckets

Space for several product photos (we’ve uploaded images)

Clean industrial aesthetic

Back of brochure:

More detailed visual layout of products

Strong callout section showing companies we represent (logos included)

Optional short paragraph about Tovrix’s capabilities, history, or differentiators

Contact info section

Overall style:

Clean, modern, print-ready

Industrial yet polished

Balanced visual + text layout

Color palette aligned with Tovrix brand

Final files delivered as print-ready PDF (plus editable source file if available)

We’ve uploaded product imagery, partner logos, and reference materials. Please design multiple layout concepts if possible.

```html
<!DOCTYPE html>
<html lang="en">
<head>
<meta charset="utf-8">
<title>Tovrix Brochure – Back and Front</title>
<link rel="stylesheet" href="https://fonts.googleapis.com/css2?family=Poppins:wght@400;500;600;700;800&display=swap">
<style>
  :root {
    --brand-blue: #1847a8;
    --accent-cyan: #36b5ea;
    --ink: #1d2530;
    --partner-ink: #3a3d42;
    --paper: #ffffff;
    --backdrop: #ebebeb;
  }
  * { box-sizing: border-box; margin: 0; padding: 0; }
  html, body { width: 800px; height: 1200px; overflow: hidden; background: var(--backdrop); }
  body { font-family: "Poppins", Arial, sans-serif; color: var(--ink); position: relative; }

  .sheet { position: absolute; top: 326px; width: 800px; height: 1130px; background: var(--paper); overflow: hidden; transform: scale(0.485); transform-origin: 0 0; box-shadow: 0 6px 24px rgba(0,0,0,0.18); }
  .sheet--back { left: 8px; }
  .sheet--front { left: 404px; }
  .sheet-shapes { position: absolute; inset: 0; }
  .abs { position: absolute; white-space: nowrap; }

  .brand-name { left: 39px; top: 30px; font-size: 60px; font-weight: 800; color: var(--brand-blue); letter-spacing: 1px; line-height: 1; }

  /* front */
  .hero-kicker { left: 36px; top: 180px; font-size: 19px; font-weight: 500; color: var(--accent-cyan); }
  .hero-title { left: 36px; top: 214px; font-size: 29px; font-weight: 800; color: #fff; line-height: 37px; }
  .hero-summary { left: 36px; top: 350px; padding-left: 10px; border-left: 2px solid var(--accent-cyan); font-size: 14px; line-height: 18px; color: #fff; }

  .service-title { font-size: 19px; font-weight: 600; color: #fff; line-height: 24px; }
  .service-text { font-size: 14px; line-height: 20px; color: #fff; }

  .category-title { left: 36px; top: 504px; font-size: 19px; font-weight: 700; color: var(--brand-blue); }
  .category-list { list-style: none; }
  .category-list li { position: absolute; left: 36px; padding-left: 15px; font-size: 14px; line-height: 19px; color: var(--ink); white-space: nowrap; }
  .category-list li::before { content: ""; position: absolute; left: 0; top: 7px; width: 5px; height: 5px; border-radius: 50%; background: var(--accent-cyan); }

  /* back */
  .cap-kicker { left: 37px; top: 579px; font-size: 15px; font-weight: 500; color: var(--accent-cyan); }
  .cap-title { left: 37px; top: 606px; font-size: 26px; font-weight: 800; color: #fff; line-height: 34px; }
  .cap-rule { left: 37px; top: 652px; width: 62px; height: 3px; background: var(--accent-cyan); }
  .cap-text { left: 37px; top: 675px; font-size: 13px; line-height: 17.7px; color: #fff; }
  .cap-list { list-style: none; }
  .cap-list li { position: absolute; left: 37px; padding-left: 12px; font-size: 13px; line-height: 17px; color: #fff; white-space: nowrap; }
  .cap-list li::before { content: ""; position: absolute; left: 0; top: 6px; width: 5px; height: 5px; border-radius: 50%; background: var(--accent-cyan); }

  .partner-card { position: absolute; left: 487px; width: 244px; height: 92px; background: #fff; box-shadow: 3px 4px 8px rgba(0,0,0,0.22); display: flex; align-items: center; justify-content: center; font-size: 22px; font-weight: 700; color: var(--partner-ink); white-space: nowrap; }

  /* footer */
  .footer-phone { left: 38px; top: 1071px; font-size: 22px; font-weight: 700; color: #fff; display: flex; align-items: center; gap: 8px; }
  .footer-link { top: 1075px; font-size: 16px; font-weight: 500; color: var(--ink); display: flex; align-items: center; gap: 5px; }
</style>
</head>
<body>

<!-- BACK SIDE -->
<section class="sheet sheet--back">
  <svg class="sheet-shapes" width="800" height="1130" viewBox="0 0 800 1130">
    <defs>
      <linearGradient id="back-grad-worker" x1="0" y1="0" x2="0" y2="1">
        <stop offset="0" stop-color="#b8ab98"/>
        <stop offset="0.35" stop-color="#7c7468"/>
        <stop offset="0.52" stop-color="#2b2b2d"/>
        <stop offset="1" stop-color="#0e0e10"/>
      </linearGradient>
      <linearGradient id="back-grad-building" x1="0" y1="0" x2="1" y2="1">
        <stop offset="0" stop-color="#6f9fd6"/>
        <stop offset="0.5" stop-color="#e6e8ec"/>
        <stop offset="1" stop-color="#c9ccd1"/>
      </linearGradient>
      <linearGradient id="back-grad-parts" x1="0" y1="0" x2="1" y2="1">
        <stop offset="0" stop-color="#a79b88"/>
        <stop offset="1" stop-color="#6b665e"/>
      </linearGradient>
      <linearGradient id="back-grad-bar" x1="0" y1="0" x2="0" y2="1">
        <stop offset="0" stop-color="#c99a55"/>
        <stop offset="0.5" stop-color="#8f8a82"/>
        <stop offset="1" stop-color="#b48648"/>
      </linearGradient>
      <linearGradient id="back-grad-rods" x1="0" y1="0" x2="1" y2="1">
        <stop offset="0" stop-color="#cfcbc4"/>
        <stop offset="1" stop-color="#7c766d"/>
      </linearGradient>
    </defs>

    <g role="img" aria-label="Craftsman drilling a steel part at a workbench">
      <polygon points="0,124 517,124 297,1063 0,1063" fill="url(#back-grad-worker)"/>
    </g>
    <g role="img" aria-label="Exterior of the Tovrix facility with company sign">
      <polygon points="568,0 800,0 800,199 521,199" fill="url(#back-grad-building)"/>
    </g>
    <g role="img" aria-label="Rows of machined steel sheller parts">
      <polygon points="517,217 800,217 800,417 471,417" fill="url(#back-grad-parts)"/>
    </g>
    <polygon points="383,807 494,1063 290,1063" fill="var(--accent-cyan)"/>
    <g role="img" aria-label="Stack of round steel rods">
      <polygon points="300,980 400,900 470,990 390,1063 300,1063" fill="url(#back-grad-rods)"/>
    </g>
    <g role="img" aria-label="Long steel sheller bar on a wooden bench">
      <polygon points="470,932 800,932 800,1063 440,1063" fill="url(#back-grad-bar)"/>
    </g>

    <polygon points="0,1063 318,1063 345,1130 0,1130" fill="var(--brand-blue)"/>
    <polygon points="318,1063 330,1063 357,1130 345,1130" fill="var(--accent-cyan)"/>
  </svg>

  <div class="abs brand-name">TOVRIX</div>

  <div class="partner-card" style="top:452px;">Norvale Industries</div>
  <div class="partner-card" style="top:574px;">Kestrolo</div>
  <div class="partner-card" style="top:695px;">Mellin Pike</div>
  <div class="partner-card" style="top:817px;">Brannick Screen Co.</div>

  <p class="abs cap-kicker">Our Capabilities</p>
  <h2 class="abs cap-title">What We Do</h2>
  <div class="abs cap-rule"></div>
  <p class="abs cap-text">At TOVRIX, Inc., we manufacture and<br>distribute replacement parts for peanut<br>processing equipment. American-made,<br>high-quality parts that are designed to<br>work great in your equipment. We have<br>been producing, reliable products<br>at our facility Marlow, Georgia<br>since 1996.</p>
  <ul class="cap-list">
    <li style="top:833px;">Replacement Parts<br>Manufacturing</li>
    <li style="top:877px;">Equipment Manufacturing</li>
    <li style="top:906px;">Replacement Parts Distribution</li>
    <li style="top:934px;">Welding &amp; Fabrication</li>
    <li style="top:963px;">Sheller Equipment<br>Refurbishing</li>
    <li style="top:1007px;">Customer Support</li>
  </ul>

  <div class="abs footer-phone">
    <svg width="22" height="22" viewBox="0 0 24 24" aria-hidden="true"><path fill="#fff" d="M6.6 10.8a15 15 0 0 0 6.6 6.6l2.2-2.2c.3-.3.7-.4 1-.2 1.1.4 2.3.6 3.6.6.6 0 1 .4 1 1V20c0 .6-.4 1-1 1A17 17 0 0 1 3 4c0-.6.4-1 1-1h3.5c.6 0 1 .4 1 1 0 1.3.2 2.5.6 3.6.1.3 0 .7-.2 1z"/></svg>
    (555) 201-4470
  </div>
  <div class="abs footer-link" style="left:346px;">
    <svg width="14" height="12" viewBox="0 0 14 12" aria-hidden="true"><rect width="14" height="12" rx="1.5" fill="var(--brand-blue)"/><path d="M1 1.5l6 5 6-5" stroke="#fff" stroke-width="1.4" fill="none"/></svg>
    dana@tovrixinc.com
  </div>
  <div class="abs footer-link" style="left:568px;">
    <svg width="14" height="14" viewBox="0 0 14 14" aria-hidden="true"><g fill="none" stroke="var(--brand-blue)" stroke-width="1.3"><circle cx="7" cy="7" r="6"/><ellipse cx="7" cy="7" rx="2.5" ry="6"/><path d="M1 7h12"/></g></svg>
    www.tovrix-inc.com
  </div>
</section>

<!-- FRONT SIDE -->
<section class="sheet sheet--front">
  <svg class="sheet-shapes" width="800" height="1130" viewBox="0 0 800 1130">
    <defs>
      <linearGradient id="grad-peanuts" x1="0" y1="0" x2="1" y2="1">
        <stop offset="0" stop-color="#8a8d94"/>
        <stop offset="0.45" stop-color="#c07a42"/>
        <stop offset="1" stop-color="#a45a28"/>
      </linearGradient>
      <linearGradient id="grad-hero" x1="0" y1="0" x2="1" y2="0">
        <stop offset="0" stop-color="#5e4434"/>
        <stop offset="1" stop-color="#86654c"/>
      </linearGradient>
      <linearGradient id="grad-steel" x1="0" y1="0" x2="1" y2="1">
        <stop offset="0" stop-color="#c9c8c4"/>
        <stop offset="1" stop-color="#7d7b78"/>
      </linearGradient>
      <linearGradient id="grad-balls" x1="0" y1="0" x2="1" y2="1">
        <stop offset="0" stop-color="#efe6cf"/>
        <stop offset="1" stop-color="#8a8478"/>
      </linearGradient>
      <linearGradient id="grad-fabric" x1="0" y1="0" x2="1" y2="1">
        <stop offset="0" stop-color="#d9cdb5"/>
        <stop offset="1" stop-color="#8f8573"/>
      </linearGradient>
      <radialGradient id="grad-bearing" cx="0.4" cy="0.4" r="0.6">
        <stop offset="0" stop-color="#e2e0db"/>
        <stop offset="1" stop-color="#6f6b66"/>
      </radialGradient>
    </defs>

    <g role="img" aria-label="Peanuts moving along a processing conveyor">
      <polygon points="604,0 800,0 800,365 408,365" fill="url(#grad-peanuts)"/>
    </g>
    <g role="img" aria-label="Close view of a bed of shelled peanuts">
      <polygon points="0,131 518,131 337,473 0,473" fill="url(#grad-hero)"/>
    </g>

    <polygon points="402,376 800,376 800,756 425,756 341,476" fill="var(--brand-blue)"/>

    <g role="img" aria-label="Perforated metal flat screen">
      <polygon points="256,768 472,768 496,909 280,909" fill="url(#grad-steel)"/>
    </g>
    <g role="img" aria-label="Herringbone sheller grate">
      <polygon points="480,768 690,768 714,909 504,909" fill="url(#grad-steel)"/>
    </g>
    <g role="img" aria-label="Coiled steel spiral parts">
      <polygon points="698,768 800,768 800,909 722,909" fill="url(#grad-steel)"/>
    </g>
    <g role="img" aria-label="Tray of rubber gum balls">
      <polygon points="298,918 474,918 498,1060 322,1060" fill="url(#grad-balls)"/>
    </g>
    <g role="img" aria-label="Rolled fiberglass sheets being marked by hand">
      <polygon points="482,918 800,918 800,1060 506,1060" fill="url(#grad-fabric)"/>
    </g>
    <g role="img" aria-label="Eccentric bearing housing">
      <ellipse cx="361" cy="728" rx="56" ry="50" fill="url(#grad-bearing)"/>
    </g>

    <g fill="none" stroke="#7fc4ef" stroke-width="2">
      <circle cx="421" cy="438" r="14"/>
      <circle cx="421" cy="438" r="6"/>
      <path d="M421 420v6M421 450v6M403 438h6M433 438h6M408 425l4 4M430 447l4 4M434 425l-4 4M412 447l-4 4"/>
    </g>
    <g fill="none" stroke="#7fc4ef" stroke-width="2">
      <circle cx="443" cy="553" r="17"/>
      <ellipse cx="443" cy="553" rx="7" ry="17"/>
      <path d="M426 553h34M429 544h28M429 562h28"/>
    </g>
    <g fill="none" stroke="#7fc4ef" stroke-width="2">
      <path d="M450 654h28l7 9-21 22-21-22z M443 663h42 M457 654l7 31 7-31"/>
    </g>

    <polygon points="0,1063 318,1063 345,1130 0,1130" fill="var(--brand-blue)"/>
    <polygon points="318,1063 330,1063 357,1130 345,1130" fill="var(--accent-cyan)"/>
  </svg>

  <div class="abs brand-name">TOVRIX</div>

  <p class="abs hero-kicker">We Manufacture &amp; Supply</p>
  <h1 class="abs hero-title">Replacement Parts<br>for Peanut Processing<br>Equipment</h1>
  <p class="abs hero-summary">Our capabilities include peanut shelling<br>equipment replacement parts, parts<br>manufacturing, equipment repair and<br>equipment refurbishing.</p>

  <h2 class="abs service-title" style="left:454px;top:426px;">Replacement Parts</h2>
  <p class="abs service-text" style="left:398px;top:470px;">Quality replacement parts<br>built to customers' specifications.</p>

  <h2 class="abs service-title" style="left:475px;top:541px;">Support</h2>
  <p class="abs service-text" style="left:419px;top:581px;">Contact us for immediate service. 7:00-4:00<br>CST – (555) 318-2906</p>

  <h2 class="abs service-title" style="left:497px;top:653px;">Service</h2>
  <p class="abs service-text" style="left:440px;top:694px;">We've been serving the peanut processing<br>industry since 1996.</p>

  <h2 class="abs category-title">Product Category</h2>
  <ul class="category-list">
    <li style="top:545px;">Flat Screens (slot, round, herringbone,<br>square, Style 1 &amp; Style 2)</li>
    <li style="top:602px;">Sheller Grates</li>
    <li style="top:640px;">Ripple Screens</li>
    <li style="top:677px;">Sheller Bars</li>
    <li style="top:715px;">Eccentric Bearing Housings</li>
    <li style="top:753px;">Eccentric Shafts</li>
    <li style="top:790px;">Rebuilt Machines</li>
    <li style="top:828px;">Ducts</li>
    <li style="top:865px;">Sprockets</li>
    <li style="top:903px;">Rubber Gum Balls</li>
    <li style="top:941px;">Fiberglass</li>
    <li style="top:978px;">Mellin Pike Reels</li>
    <li style="top:1016px;">Elevator Buckets</li>
  </ul>

  <div class="abs footer-phone">
    <svg width="22" height="22" viewBox="0 0 24 24" aria-hidden="true"><path fill="#fff" d="M6.6 10.8a15 15 0 0 0 6.6 6.6l2.2-2.2c.3-.3.7-.4 1-.2 1.1.4 2.3.6 3.6.6.6 0 1 .4 1 1V20c0 .6-.4 1-1 1A17 17 0 0 1 3 4c0-.6.4-1 1-1h3.5c.6 0 1 .4 1 1 0 1.3.2 2.5.6 3.6.1.3 0 .7-.2 1z"/></svg>
    (555) 201-4470
  </div>
  <div class="abs footer-link" style="left:346px;">
    <svg width="14" height="12" viewBox="0 0 14 12" aria-hidden="true"><rect width="14" height="12" rx="1.5" fill="var(--brand-blue)"/><path d="M1 1.5l6 5 6-5" stroke="#fff" stroke-width="1.4" fill="none"/></svg>
    dana@tovrixinc.com
  </div>
  <div class="abs footer-link" style="left:568px;">
    <svg width="14" height="14" viewBox="0 0 14 14" aria-hidden="true"><g fill="none" stroke="var(--brand-blue)" stroke-width="1.3"><circle cx="7" cy="7" r="6"/><ellipse cx="7" cy="7" rx="2.5" ry="6"/><path d="M1 7h12"/></g></svg>
    www.tovrix-inc.com
  </div>
</section>

</body>
</html>
```